Employees at T&M Gale Power Solutions need new modern business cards

We need new business cards that showcase our new rebranded logo. We are seeking modern, clean, fresh, attractive cards while still being professional. We want to stand out. A little bit about us: we work in Canada and the USA. We offer Technical Field Advisors to support wind turbine manufacturers through the construction phase of wind farms. I am attaching a mock inspiration picture to lead you in the direction we want to see this go. Also, FYI We have approx. 10/11 different employees that would need their own card. Let me know when you would need everyone's name. We would love to see some black and white options as well as color copies- when using colors we want green to be the dominant color with accents for blue and orange (colors should match our logo). I have also attached copies of our old business card for reference.

Contact Information for Business Card

Name, Telephone, Email, address, company name, website. EXAMPLE: Hugh Marlow, HughMarlow@tandmgale.example, 555-381-4926, 217763 Birch Line #9, Elmhurst, ON X1Y 2Z3, www.tandmgale.example

Colors
0054AA
0677BA
7BADD7
CADEEF
E8F1F8
00AB8E
00BBA5
67D7C9
C6EFE9
E9F9F6
F0912C
F2A743
F7CA91
FBE8D2
FDF5EE

Requirements
Must have
• 2 sided business card

```html
<!DOCTYPE html>
<html lang="en">
<head>
<meta charset="utf-8">
<title>T&amp;M Gale Power Solutions – Business Card</title>
<link href="https://fonts.googleapis.com/css2?family=Montserrat:wght@400;500;700;800&display=swap" rel="stylesheet">
<style>
  :root {
    --page-bg: #161616;
    --card-bg: #252525;
    --card-edge: #1d1d1d;
    --brand-green: #3bb54a;
    --brand-orange: #f0912c;
    --brand-yellow: #fcc419;
    --brand-blue: #0677ba;
    --text-light: #f2f2f2;
    --emboss: #303030;
    --emboss-hi: #3a3a3a;
  }
  * { box-sizing: border-box; margin: 0; padding: 0; }
  html, body {
    width: 1200px; height: 900px; overflow: hidden;
    background: var(--page-bg);
    font-family: "Montserrat", sans-serif;
  }
  .sheet {
    width: 1200px; height: 900px;
    display: flex; flex-direction: column;
    align-items: center; justify-content: center; gap: 56px;
  }
  .card {
    position: relative;
    width: 660px; height: 377px;
    background: var(--card-bg);
    border-radius: 22px;
    overflow: hidden;
    box-shadow: 0 18px 40px rgba(0,0,0,.55);
  }
  .card__stripe {
    position: absolute; left: 0; right: 0; bottom: 0; height: 12px;
    background: linear-gradient(90deg,
      var(--brand-green) 0 44%,
      var(--brand-orange) 44%, var(--brand-yellow) 60%, var(--brand-orange) 72%,
      var(--brand-blue) 72% 100%);
  }

  /* front */
  .brand {
    position: absolute; top: 58px; left: 250px;
    display: flex; align-items: center; gap: 12px;
  }
  .brand__dot {
    width: 34px; height: 34px; border-radius: 50%;
    background: var(--brand-green);
  }
  .brand__name {
    font-weight: 800; font-size: 19px; letter-spacing: 1px;
    text-transform: uppercase; color: var(--brand-green);
  }
  .identity {
    position: absolute; top: 150px; left: 40px; width: 290px;
    text-align: right;
  }
  .identity__name {
    font-weight: 800; font-size: 30px; letter-spacing: 1px;
    color: var(--brand-green); text-transform: uppercase;
  }
  .identity__title {
    font-weight: 400; font-size: 18px; color: var(--text-light);
    margin-top: 4px;
  }
  .divider {
    position: absolute; top: 150px; left: 348px;
    width: 1.5px; height: 86px; background: var(--brand-orange);
  }
  .contacts {
    position: absolute; top: 150px; left: 366px;
    list-style: none;
  }
  .contacts__item {
    display: flex; align-items: center; gap: 8px;
    font-size: 15px; color: var(--text-light);
    height: 29px;
  }
  .contacts__icon { width: 15px; height: 15px; flex: none; }
  .address {
    position: absolute; top: 268px; left: 70px;
    font-size: 17px; color: var(--text-light);
  }

  /* back */
  .brand--embossed {
    position: absolute; top: 50%; left: 50%;
    transform: translate(-50%, -58%);
    display: flex; flex-direction: column; align-items: center; gap: 18px;
  }
  .brand--embossed .brand__dot {
    width: 110px; height: 110px;
    background: var(--emboss);
    box-shadow: inset 2px 2px 3px var(--emboss-hi), inset -2px -2px 4px #1a1a1a;
  }
  .brand--embossed .brand__name {
    font-size: 32px; color: var(--emboss);
    text-align: center;
  }
</style>
</head>
<body>
<main class="sheet">

  <section class="card card--front" aria-label="Card front">
    <div class="brand">
      <span class="brand__dot"></span>
      <span class="brand__name">T&amp;M Gale Power Solutions</span>
    </div>

    <div class="identity">
      <p class="identity__name">Hugh Marlow</p>
      <p class="identity__title">CEO/Founder</p>
    </div>

    <div class="divider"></div>

    <ul class="contacts">
      <li class="contacts__item">
        <svg class="contacts__icon" viewBox="0 0 24 24"><path fill="#f0912c" d="M6.6 10.8a15.5 15.5 0 0 0 6.6 6.6l2.2-2.2c.3-.3.7-.4 1-.2 1.1.4 2.3.6 3.6.6.6 0 1 .4 1 1V20c0 .6-.4 1-1 1A17 17 0 0 1 3 4c0-.6.4-1 1-1h3.5c.6 0 1 .4 1 1 0 1.3.2 2.5.6 3.6.1.3 0 .7-.2 1z"/></svg>
        555-381-4926
      </li>
      <li class="contacts__item">
        <svg class="contacts__icon" viewBox="0 0 24 24"><rect x="2" y="5" width="20" height="14" rx="2" fill="#f0912c"/><path d="M3 6l9 7 9-7" fill="none" stroke="#252525" stroke-width="1.8"/></svg>
        HughMarlow@tandmgale.example
      </li>
      <li class="contacts__item">
        <svg class="contacts__icon" viewBox="0 0 24 24" fill="none" stroke="#f0912c" stroke-width="2"><circle cx="12" cy="12" r="9"/><path d="M3 12h18M12 3c3 3 3 15 0 18M12 3c-3 3-3 15 0 18"/></svg>
        www.tandmgale.example
      </li>
    </ul>

    <p class="address">217763 Birch Line #9, Elmhurst, ON X1Y 2Z3</p>

    <div class="card__stripe"></div>
  </section>

  <section class="card card--back" aria-label="Card back">
    <div class="brand brand--embossed">
      <span class="brand__dot"></span>
      <span class="brand__name">T&amp;M Gale Power Solutions</span>
    </div>
    <div class="card__stripe"></div>
  </section>

</main>
</body>
</html>
```